Hacienda Las Verbenas Website

I need a template design for Hacienda Las Verbenas which is a Residential and Commercial development project to be located in Panama.

The look of the website has to be "country" since it is a Hacienda. It has to take in the feel of being out with nature.

The Logo of the project is contained in the attached files as well as pictures of the Project´s conceptual design and several air pictures of the land where the project will be built.

Industry/Entity Type

Residential

Requirements
Must have
• The website has to be very simple, very visual, a lot of images. The Main Menu has to be:
1. Home
2. About us
3. The project
4. Location
5. Contact us

```html
<!DOCTYPE html>
<html lang="en">
<head>
<meta charset="utf-8">
<title>Hacienda Las Verbenas</title>
<link href="https://fonts.googleapis.com/css2?family=Lato:wght@300;400;700&display=swap" rel="stylesheet">
<style>
:root{
  --gold:#c4922e;
  --gold-dark:#a57a22;
  --brown:#6b4632;
  --text:#555;
  --muted:#9a9a9a;
  --line:#e3e3e3;
  --footer:#efefef;
  --white:#fff;
}
*{margin:0;padding:0;box-sizing:border-box}
html,body{width:747px;height:1200px;overflow:hidden;background:var(--white)}
body{position:relative;font-family:"Lato",Arial,sans-serif;color:var(--text)}
.abs{position:absolute}
.topbar{left:0;top:0;width:747px;height:31px;background:var(--gold)}
.search{left:380px;top:7px;width:161px;height:16px;background:var(--gold-dark);border-radius:3px;color:#fff;font-size:6.5px;padding:4px 5px}
.search svg{position:absolute;right:5px;top:3px}
.help{left:590px;top:9px;font-size:8.5px;color:#f3e3c0}
.brand{left:88px;top:57px;font-size:15px;font-weight:400;color:var(--brown);white-space:nowrap}
.nav{left:358px;top:57px;display:flex;gap:17px;font-size:12.5px;font-weight:300}
.nav a{color:#555;text-decoration:none}
.nav a.active{color:var(--gold)}
.hero{left:0;top:98px;width:747px;height:299px;background:linear-gradient(135deg,#3f6a2c,#6f8f47 45%,#8c9a6a 65%,#4d7733)}
.caption{left:105px;top:208px;width:281px;height:105px;background:rgba(40,40,30,.55);padding:7px 16px;color:#fff;font-weight:300}
.caption .l1{font-size:14px;line-height:18px}
.caption .l2{font-size:23px;line-height:26px}
.caption .l3{font-size:44px;line-height:46px;color:var(--gold)}
.arrow{width:38px;height:38px;border-radius:50%;background:rgba(255,255,255,.55);top:229px}
.arrow svg{position:absolute;left:12px;top:11px}
h2{position:absolute;font-size:12.5px;font-weight:400;color:#333}
.rule{position:absolute;height:1px;background:var(--line)}
.photo{position:absolute}
.body-text{font-size:8.5px;line-height:15px;color:var(--muted);text-align:justify;font-weight:300}
.body-text p+p{margin-top:15px}
.card{position:absolute;width:137px;top:802px}
.card .photo{position:static;height:82px;background:linear-gradient(160deg,#6e8f4f,#3e6a2c)}
.card h3{font-size:9px;font-weight:400;color:#333;margin-top:13px}
.card p{font-size:7.3px;line-height:15px;color:var(--muted);margin-top:3px;text-align:justify;font-weight:300}
.btn{display:inline-block;margin-top:11px;background:var(--brown);color:#f3e3d0;font-size:9px;padding:4px 8px;font-weight:300}
.badges{left:85px;top:1031px;width:580px;display:flex;justify-content:space-between;align-items:center}
.badges span{display:block;width:50px;height:24px;background:#d6d6d6;border-radius:2px}
.signup{left:81px;top:1090px;width:584px;height:56px;background:var(--gold)}
.signup .label{position:absolute;left:17px;top:18px;font-size:14px;font-weight:300;color:#fff}
.signup .field{position:absolute;left:240px;top:17px;width:248px;height:25px;background:#fff;font-size:7px;color:#aaa;padding:8px}
.signup .submit{position:absolute;left:500px;top:17px;width:64px;height:23px;background:var(--brown);color:#f3e3d0;font-size:8.5px;text-align:center;line-height:23px}
.footer{left:0;top:1146px;width:747px;height:54px;background:var(--footer)}
.footer .links{position:absolute;left:80px;top:13px;font-size:9px;color:#444}
.footer .links span{margin:0 8px;color:#777}
.footer .copy{position:absolute;left:80px;top:30px;font-size:9px;color:#444}
.social{position:absolute;top:20px;display:flex;gap:8px;left:568px}
.social span{width:19px;height:19px;border-radius:3px;background:#b5b5b5}
</style>
</head>
<body>
<div class="abs topbar"></div>
<div class="abs search">Search
  <svg width="10" height="10" viewBox="0 0 10 10"><circle cx="4" cy="4" r="3" fill="none" stroke="#fff" stroke-width="1.4"/><line x1="6.2" y1="6.2" x2="9" y2="9" stroke="#fff" stroke-width="1.6"/></svg>
</div>
<div class="abs help">Help | Contact Us</div>

<div class="abs brand">Hacienda Las Verbenas</div>
<nav class="abs nav">
  <a class="active" href="#">Home</a><a href="#">About us</a><a href="#">The project</a><a href="#">Location</a><a href="#">Contact us</a>
</nav>

<div class="abs hero" role="img" aria-label="Aerial view of green countryside with a highway crossing the land"></div>
<div class="abs caption">
  <div class="l1">Its a Residential and Commercial</div>
  <div class="l2">Development Project</div>
  <div class="l3">in Panama</div>
</div>
<div class="abs arrow" style="left:34px"><svg width="12" height="16" viewBox="0 0 12 16"><polyline points="10,1 2,8 10,15" fill="none" stroke="#888" stroke-width="2"/></svg></div>
<div class="abs arrow" style="left:675px"><svg width="12" height="16" viewBox="0 0 12 16"><polyline points="2,1 10,8 2,15" fill="none" stroke="#888" stroke-width="2"/></svg></div>

<h2 style="left:78px;top:413px">Welcome to Las Verbenas</h2>
<div class="rule" style="left:80px;top:433px;width:287px"></div>
<div class="photo" style="left:81px;top:442px;width:286px;height:103px;background:linear-gradient(180deg,#2a2320,#5a4530 60%,#20252e)" role="img" aria-label="City skyline lit up at night over the bay"></div>
<div class="abs body-text" style="left:81px;top:565px;width:286px">
  <p>Sed ut perspiciatis unde omnis iste natus error sit voluptatem accusantium doloremque laudantium, totam rem aperiam, eaque ipsa quae ab illo inventore veritatis et quasi architecto beatae vitae dicta sunt explicabo. Nemo enim ipsam voluptatem quia voluptas sit aspernatur aut odit aut fugit, sed quia consequuntur magni dolores eos qui ratione voluptatem sequi nesciunt.</p>
  <p>Totam rem aperiam, eaque ipsa quae ab illo inventore veritatis et quasi architecto beatae vitae dicta sunt explicabo. Nemo enim ipsam voluptatem quia voluptas sit aspernatur aut odit aut fugit, sed quia consequuntur magni dolores eos qui ratione voluptatem sequi nesciunt.</p>
</div>

<h2 style="left:416px;top:413px">Our Plans</h2>
<div class="rule" style="left:416px;top:433px;width:251px"></div>
<div class="photo" style="left:417px;top:442px;width:249px;height:103px;background:linear-gradient(180deg,#7aa4c8,#5f8a3e 45%,#8a8a8a 75%,#6b9a48)" role="img" aria-label="Rendering of a tree-lined entrance road"></div>
<div class="abs body-text" style="left:418px;top:555px;width:248px">Sed ut perspiciatis unde omnis iste natus error sit voluptatem accusantium doloremque laudantium...</div>
<div class="photo" style="left:418px;top:599px;width:249px;height:104px;background:linear-gradient(180deg,#5d8fd0,#a9c4e0 45%,#a0603a 60%,#5f8a3e)" role="img" aria-label="Rendering of the brick entrance gate of the development"></div>
<div class="abs body-text" style="left:418px;top:712px;width:248px">Sed ut perspiciatis unde omnis iste natus error sit voluptatem accusantium doloremque laudantium...</div>

<h2 style="left:81px;top:763px">Latest Projects</h2>
<svg class="abs" style="left:644px;top:769px" width="20" height="12" viewBox="0 0 20 12"><polyline points="6,1 1,6 6,11" fill="none" stroke="#222" stroke-width="2"/><polyline points="14,1 19,6 14,11" fill="none" stroke="#222" stroke-width="2"/></svg>
<div class="rule" style="left:0;top:787px;width:747px"></div>

<div class="card" style="left:81px"><div class="photo" role="img" aria-label="Aerial view of the site with the highway"></div><h3>Project Name : LasVerbenas</h3><p>Description : Lorem ipsum dolor sit amet, consectetur adipisicing elit, sed do eiusmod tempor incididunt ut labore et dolore magna aliqua</p><span class="btn">Read More</span></div>
<div class="card" style="left:231px"><div class="photo" role="img" aria-label="Aerial view of cleared land"></div><h3>Project Name : LasVerbenas</h3><p>Description : Lorem ipsum dolor sit amet, consectetur adipisicing elit, sed do eiusmod tempor incididunt ut labore et dolore magna aliqua</p><span class="btn">Read More</span></div>
<div class="card" style="left:380px"><div class="photo" role="img" aria-label="Aerial view of fields beside the road"></div><h3>Project Name : LasVerbenas</h3><p>Description : Lorem ipsum dolor sit amet, consectetur adipisicing elit, sed do eiusmod tempor incididunt ut labore et dolore magna aliqua</p><span class="btn">Read More</span></div>
<div class="card" style="left:529px"><div class="photo" role="img" aria-label="Aerial view of green hills"></div><h3>Project Name : LasVerbenas</h3><p>Description : Lorem ipsum dolor sit amet, consectetur adipisicing elit, sed do eiusmod tempor incididunt ut labore et dolore magna aliqua</p><span class="btn">Read More</span></div>

<div class="abs badges" aria-label="Partners"><span></span><span></span><span></span><span></span><span></span><span></span><span></span><span></span></div>

<div class="abs signup">
  <div class="label">Sign up for weekly sermon tips</div>
  <div class="field">Enter Your E-mail address</div>
  <div class="submit">SUBMIT</div>
</div>

<footer class="abs footer">
  <div class="links">Home<span>|</span>About us<span>|</span>The project<span>|</span>Location<span>|</span>Contact us</div>
  <div class="copy">©2013 Company Name , All Rights Reserved</div>
  <div class="social"><span></span><span></span><span></span><span></span></div>
</footer>
</body>
</html>
```